Sticker label design for - Tidal Fern Deodorant Balm

I need a label for my 100% Natural Deodorant Balm
The brand is called "Plum Meadow Brand", and the product is called TIDAL FERN Deodorant Balm.
There are two labels, one is a 5.2cm circle for the top, and 4.5cm circle for the base. The jar is amber plastic with black lid.
Width: 5.8cm
Height: 3.4cm (Lid 1.2cm, base 2,2cm)
Here is a link to what the jar looks like from one of my competitors: https://copperwren.com.au/products/body/velaro-deodorant-paste/
The product is a unisex product. Please see uploaded files for designs previously made for the brand. I'm trying to see a few more designs before finalising my choice. Feel free to use the logo at the top (Plum Meadow Brand) of either attachment if you would like. Or design your own.
Be be aware that it is meant to be Aluminium and Paraben Free, not "Parabens" Weight of product is 70g, please include this.
Label can be any colour, and printed with regular colours or event gold, silver or rose gold foil. Would a background be nice?
This is something I saw that I liked:
http://www.mossvelbalm.com
However I'm really open to what people can come up with.
For the back base-
Tidal Fern deodorant balm is made from 100% natural ingredients, and works by neutralises odour and minimising wetness without the use of harmful chemicals.
www.plummeadowbrand.com
Directions: For optimal result, apply a pea size amount of the balm to your dry armpits. Gently rub the balm into your armpits covering the entire area. Discontinue use if irritation occurs.
Ingredients: Shea Butter, Coconut oil, Sodium Bicarbonate, Arrowroot, Kaolin Clay, Vitamin E, Vegetable Glycerin, Activated Charcoal, Essential oils of Peppermint, Lavender, Mandarin, Tea tree, Geranium Rose & Cedarwood.
MADE IN AUSTRALIA
Reason: Hi,
I'm not getting many submissions, so was hoping to extend the deadline.
Skin Care Product

```html
<!DOCTYPE html>
<html lang="en">
<head>
<meta charset="utf-8">
<title>Tidal Fern Deodorant Balm – Labels</title>
<link rel="stylesheet" href="https://fonts.googleapis.com/css2?family=Oswald:wght@600&family=Lato:wght@400;700;900&family=Yellowtail&display=swap">
<style>
  :root {
    --ink: #1c1c1c;
    --page: #ffffff;
    --stone-light: #e6eeed;
    --stone-mid: #cfdcdc;
    --stone-deep: #b9cacb;
    --back-fill: #e2f3f6;
  }
  * { box-sizing: border-box; margin: 0; padding: 0; }
  html, body {
    width: 858px;
    height: 1200px;
    overflow: hidden;
    background: var(--page);
  }
  body {
    position: relative;
    color: var(--ink);
    font-family: "Lato", sans-serif;
  }
  .label {
    position: absolute;
    left: 149px;
    width: 560px;
    height: 560px;
    border-radius: 50%;
    overflow: hidden;
  }
  .label--top { top: 25px; }
  .label--base { top: 615px; background: var(--back-fill); }

  .stone-texture {
    position: absolute;
    inset: 0;
    background:
      linear-gradient(155deg, transparent 30%, rgba(185,202,203,0.45) 45%, transparent 55%),
      linear-gradient(150deg, transparent 55%, rgba(185,202,203,0.4) 68%, transparent 80%),
      radial-gradient(circle at 35% 30%, var(--stone-light), var(--stone-mid) 85%);
  }
  .label-art {
    position: absolute;
    inset: 0;
    width: 560px;
    height: 560px;
  }
  .centered {
    position: absolute;
    left: 0;
    width: 100%;
    text-align: center;
  }

  /* top label */
  .brand-name {
    top: 62px;
    font-weight: 900;
    font-size: 40px;
    letter-spacing: 4px;
    line-height: 1;
  }
  .brand-sub {
    top: 112px;
    font-weight: 900;
    font-size: 22px;
    letter-spacing: 10px;
    line-height: 1;
  }
  .brand-mark {
    position: absolute;
    left: 268px;
    top: 152px;
    width: 24px;
    height: 24px;
    border-radius: 50%;
    background: var(--ink);
  }
  .product-name {
    top: 232px;
    font-family: "Oswald", sans-serif;
    font-weight: 600;
    font-size: 86px;
    line-height: 1;
    letter-spacing: 2px;
  }
  .product-type {
    top: 330px;
    font-weight: 700;
    font-size: 29px;
    letter-spacing: 3.5px;
    line-height: 1;
  }
  .claim {
    top: 378px;
    display: flex;
    justify-content: center;
    align-items: center;
    gap: 16px;
  }
  .claim-text {
    font-family: "Yellowtail", cursive;
    font-size: 42px;
    line-height: 1;
  }
  .rule-pair {
    width: 62px;
    height: 8px;
    border-top: 2px solid var(--ink);
    border-bottom: 2px solid var(--ink);
  }
  .net-weight {
    top: 446px;
    font-size: 26px;
    font-weight: 400;
    line-height: 1;
  }
  .arc-text {
    font-family: "Lato", sans-serif;
    font-weight: 700;
    fill: var(--ink);
  }

  /* base label */
  .base-title {
    top: 72px;
    font-family: "Oswald", sans-serif;
    font-weight: 600;
    font-size: 42px;
    letter-spacing: 1.5px;
    line-height: 1;
  }
  .base-type {
    top: 122px;
    font-weight: 700;
    font-size: 17px;
    letter-spacing: 2.5px;
    line-height: 1;
  }
  .base-intro {
    top: 150px;
    left: 95px;
    width: 370px;
    font-size: 15.5px;
    line-height: 1.5;
  }
  .base-site {
    top: 246px;
    font-weight: 700;
    font-size: 21px;
    letter-spacing: 0.5px;
  }
  .base-details {
    position: absolute;
    top: 288px;
    left: 70px;
    width: 420px;
    font-size: 13.6px;
    line-height: 1.36;
    text-align: justify;
    text-align-last: center;
  }
  .base-details p + p { margin-top: 2px; }
  .base-details strong { font-weight: 700; }
</style>
</head>
<body>

  <section class="label label--top" aria-label="Lid label">
    <div class="stone-texture" role="img" aria-label="Soft pale blue-grey stone marble background"></div>

    <div class="centered brand-name">PLUM MEADOW</div>
    <div class="centered brand-sub">BRAND</div>
    <span class="brand-mark"></span>

    <h1 class="centered product-name">TIDAL FERN</h1>
    <div class="centered product-type">DEODORANT BALM</div>

    <div class="centered claim">
      <span class="rule-pair"></span>
      <span class="claim-text">100% Natural</span>
      <span class="rule-pair"></span>
    </div>

    <div class="centered net-weight">Wt. 70g</div>

    <svg class="label-art" viewBox="0 0 560 560" aria-hidden="false">
      <defs>
        <path id="top-bottom-arc" d="M52 280 A228 228 0 0 0 508 280"/>
      </defs>
      <text class="arc-text" font-size="25" letter-spacing="1">
        <textPath href="#top-bottom-arc" startOffset="50%" text-anchor="middle">ALUMINIUM &amp; PARABEN FREE</textPath>
      </text>
    </svg>
  </section>

  <section class="label label--base" aria-label="Base label">
    <svg class="label-art" viewBox="0 0 560 560">
      <defs>
        <path id="base-bottom-arc" d="M60 280 A220 220 0 0 0 500 280"/>
      </defs>
      <g fill="none" stroke="var(--ink)" stroke-width="2">
        <path d="M92 115 A250 250 0 0 0 88 440"/>
        <path d="M468 115 A250 250 0 0 1 472 440"/>
      </g>
      <g fill="var(--ink)">
        <polygon points="40,270 50,280 40,290 30,280"/>
        <polygon points="520,270 530,280 520,290 510,280"/>
      </g>
      <text class="arc-text" font-size="21" letter-spacing="1.5">
        <textPath href="#base-bottom-arc" startOffset="50%" text-anchor="middle">MADE IN AUSTRALIA</textPath>
      </text>
    </svg>

    <h2 class="centered base-title">TIDAL FERN</h2>
    <div class="centered base-type">DEODORANT BALM</div>

    <p class="centered base-intro">is made from 100% natural ingredients, and works by neutralises odour and minimising wetness without the use of harmful chemicals.</p>

    <div class="centered base-site">WWW.PLUMMEADOWBRAND.COM</div>

    <div class="base-details">
      <p><strong>Directions:</strong> For optimal result, apply a pea size amount of the balm to your dry armpits. Gently rub the balm into your armpits covering the entire area. Discontinue use if irritation occurs.</p>
      <p><strong>Ingredients:</strong> Shea Butter, Coconut oil, Sodium Bicarbonate, Arrowroot, Kaolin Clay, Vitamin E, Vegetable Glycerin, Activated Charcoal, Essential oils of Peppermint, Lavender, Mandarin, Tea tree, Geranium Rose &amp; Cedarwood.</p>
    </div>
  </section>

</body>
</html>
```